Web Page for marketing online agency

We are an online marketing agency that is acing the direct response model. We engage with our customers throughout different marketing techniques as research copy-writing, advertisements and content writing. We would need a website design that will have four main aspects: The Vision; stating who we are, The Mission; stating what we do, The Team And It's Values, and a Contact Form. For this design we would want a sharp, clean and smart approach, with illustrated elements or suggestive images. You can use the attached copy, the logo, the USP and the motto. Please integrate them as you see fit while keeping in mind the previous needs and copy. This website is going to be our connection with our possible partners, future colleagues and even our clients. You may submit a design for one page or integrate the 4 different aspects on separate web pages.
Target Market(s)
business partners, future employees, age range 25-60
Industry/Entity Type
Direct Marketing
Number of Pages Required
1 page
Requirements
Must have
- Menu / Header
- 4 Parts or 4 Pages including: vision, mission, team, contact
- Logo
- Motto: Direct Brilliance
- USP: We help people help themselves.
- The copy attached
Nice to have
- Representative illustrated images or elements
Should not have
- A boring design, classical design - WordPress like

```html
<!DOCTYPE html>
<html lang="en">
<head>
<meta charset="utf-8">
<title>BrightLeap — Direct Brilliance</title>
<link href="https://fonts.googleapis.com/css2?family=Lato:wght@400;700;900&family=Open+Sans:ital,wght@0,400;0,600;0,700;1,400&display=swap" rel="stylesheet">
<style>
:root{
  --blue:#2e93db;
  --blue-dark:#1f7cc0;
  --ink:#222;
  --text:#555;
  --muted:#8a8a8a;
  --grey-bg:#f1f1f1;
  --footer:#1b1b1b;
  --white:#fff;
}
*{margin:0;padding:0;box-sizing:border-box}
html,body{width:1200px;height:4276px;overflow:hidden;background:var(--white)}
body{position:relative;font-family:"Open Sans",Arial,sans-serif;color:var(--text);font-size:13px;line-height:1.7}
.abs{position:absolute}
h1,h2,h3,h4{font-family:"Lato",Arial,sans-serif;color:var(--ink)}
.section-title{font-size:30px;font-weight:900;text-align:center;letter-spacing:.5px}
.lead{text-align:center;font-size:13px;color:var(--muted)}
.read-more{font-family:"Lato",Arial,sans-serif;font-weight:700;font-size:13px;color:var(--blue);text-transform:uppercase;display:inline-flex;align-items:center;gap:6px}
.read-more i{display:inline-block;width:13px;height:13px;border-radius:50%;background:var(--blue);position:relative}
.read-more i:after{content:"";position:absolute;left:3px;top:4px;border-left:6px solid #fff;border-top:3px solid transparent;border-bottom:3px solid transparent}
.photo{border:6px solid #fff;box-shadow:0 2px 8px rgba(0,0,0,.18)}

/* header */
.site-header{left:0;top:0;width:1200px;height:128px;background:#fff}
.brand{left:100px;top:44px;font-family:"Lato",sans-serif;font-weight:900;font-size:40px;color:var(--ink);display:flex;align-items:center;gap:12px}
.brand-dot{width:22px;height:22px;border-radius:50%;background:var(--blue)}
.contact-bar{right:100px;top:32px;display:flex;gap:36px;font-size:13px;color:#444}
.contact-bar span{display:flex;align-items:center;gap:10px}
.mini-ico{width:24px;height:24px;border-radius:50%;background:#e9e9e9;display:flex;align-items:center;justify-content:center}
.main-nav{right:100px;top:80px;display:flex;gap:30px;font-family:"Lato",sans-serif;font-weight:700;font-size:15px;color:#333}
.main-nav .active{color:var(--blue)}

/* hero */
.hero{left:0;top:128px;width:1200px;height:590px;background:linear-gradient(135deg,#6b4a2c 0%,#8a6440 40%,#a57c52 70%,#7a5636 100%)}
.hero-shade{left:0;top:0;width:100%;height:100%;background:rgba(0,0,0,.25)}
.hero-line{left:0;top:712px;width:1200px;height:6px;background:var(--blue)}
.hero-title{left:0;top:286px;width:1200px;text-align:center;color:#fff;font-family:"Lato",sans-serif;font-weight:900}
.hero-title .l1{font-size:56px;line-height:1.1}
.hero-title .l2{font-size:44px;line-height:1.3}
.hero-arrow{top:407px;width:38px;height:38px;border-radius:50%;background:rgba(40,40,40,.7)}
.hero-arrow svg{display:block;margin:11px auto}

/* services */
.service{top:960px;width:230px;text-align:center}
.service-ico{width:84px;height:84px;border-radius:50%;background:var(--blue);margin:0 auto;display:flex;align-items:center;justify-content:center;box-shadow:0 0 0 6px #d7ebf8}
.service h4{margin-top:22px;font-size:14px;font-weight:700;text-transform:uppercase}
.service p{margin-top:8px;font-size:11.5px;color:var(--muted);line-height:1.65}

/* who we are */
.who{left:0;top:1254px;width:1200px;height:447px;background:linear-gradient(180deg,#fafafa,#f0f0f0)}
.who-photo{left:100px;top:1338px;width:442px;height:283px;background:linear-gradient(135deg,#3c4553,#8e9aa6 55%,#c9cfd4)}
.who-text{left:598px;top:1318px;width:500px}
.who-text h2{font-size:34px;font-weight:900}
.who-text p{margin-top:18px;font-size:13px;color:var(--muted);line-height:1.75}
.btn-pill{display:inline-flex;align-items:center;gap:6px;background:var(--blue);color:#fff;border-radius:20px;padding:8px 20px;font-family:"Lato",sans-serif;font-weight:700;font-size:13px}

/* cta band */
.cta{left:0;top:1701px;width:1200px;height:214px;background:linear-gradient(90deg,#2b8fd8,#3aa0e4)}
.cta h2{position:absolute;left:100px;top:64px;color:#fff;font-size:32px;font-weight:900}
.cta p{position:absolute;left:100px;top:118px;color:#d8ecfa;font-size:13px}
.btn-outline{position:absolute;left:943px;top:86px;width:160px;height:40px;border:2px solid #fff;border-radius:22px;color:#fff;font-family:"Lato",sans-serif;font-weight:700;font-size:13px;display:flex;align-items:center;justify-content:center}

/* case studies */
.case{top:2129px;width:302px}
.case .photo{height:174px}
.case h3{margin-top:38px;font-size:20px;font-weight:700}
.case p{margin-top:10px;font-size:11.5px;color:var(--muted);line-height:1.7;text-align:justify}
.case .read-more{margin-top:10px}

/* stats */
.stats-wave{left:0;top:2508px;width:1200px;height:342px}
.stat{top:2680px;width:240px;color:#fff}
.stat .num{font-family:"Lato",sans-serif;font-size:32px;font-weight:700;line-height:1}
.stat .num small{font-size:18px}
.stat h4{color:#fff;font-size:25px;font-weight:700;margin-top:6px}
.stat p{color:#d8ecfa;font-size:13px;line-height:1.55;margin-top:6px}

/* testimonials */
.testimonials{left:0;top:2850px;width:1200px;height:520px;background:var(--grey-bg)}
.client-photo{left:157px;top:2927px;width:180px;height:180px;border-radius:50%;background:linear-gradient(160deg,#c9c2b8,#6d6255 60%,#2e2a26);border:6px solid #fff;box-shadow:0 0 0 3px var(--blue)}
.quote-badge{left:223px;top:3077px;width:46px;height:46px;border-radius:50%;background:var(--blue);border:4px solid #fff;color:#fff;font-family:"Lato",sans-serif;font-weight:900;font-size:30px;line-height:50px;text-align:center}
.testimonial-body{left:393px;top:2920px;width:680px}
.testimonial-body h2{font-size:32px;font-weight:900}
.testimonial-body blockquote{margin-top:18px;font-style:italic;font-size:13px;color:#666;line-height:1.8}
.testimonial-body cite{display:block;margin-top:28px;font-style:normal;font-size:13px;color:#777}
.testimonial-body cite b{color:var(--blue);font-family:"Lato",sans-serif}
.side-arrow{top:3005px}

/* team */
.team-curve{left:0;top:3190px;width:1200px;height:180px}
.team-title{left:0;top:3264px;width:1200px}
.team-lead{left:300px;top:3318px;width:600px}
.member-photo{width:177px;height:165px;top:3406px}
.member-photo.a{left:100px;background:linear-gradient(160deg,#d9d6d2,#8b8580 60%,#4a4542)}
.member-photo.b{left:641px;background:linear-gradient(160deg,#4c3a2a,#2a211b 60%,#151110)}
.member-frame{top:3396px;width:60px;height:110px;border:3px solid var(--blue);border-right:none;border-bottom:none}
.member{top:3400px;width:235px}
.member h3{font-size:22px;font-weight:700}
.member .role{font-family:"Lato",sans-serif;font-weight:700;font-size:13px;color:#333;margin-top:6px}
.member p{font-size:11.5px;color:var(--muted);line-height:1.75;margin-top:10px;text-align:justify}
.member .read-more{margin-top:12px}

/* contact */
.contact{left:0;top:3662px;width:1200px;height:542px;background:linear-gradient(135deg,#2a8ad2,#3a9fe3 60%,#2b8ad0)}
.contact h2{position:absolute;left:0;top:76px;width:1200px;text-align:center;color:#fff;font-size:30px;font-weight:900}
.contact .sub{position:absolute;left:0;top:126px;width:1200px;text-align:center;color:#e3f1fb;font-size:13px}
.field{position:absolute;border:1px solid rgba(255,255,255,.85);color:#eaf5fd;font-size:12px;padding:10px 14px}
.btn-submit{position:absolute;left:519px;top:348px;width:160px;height:42px;border-radius:22px;background:#161616;color:#fff;font-family:"Lato",sans-serif;font-weight:700;font-size:14px;display:flex;align-items:center;justify-content:center}
.info{position:absolute;top:440px;display:flex;align-items:center;gap:18px;color:#fff;font-size:12px;line-height:1.6}
.info-ico{width:44px;height:44px;border-radius:50%;background:#fff;display:flex;align-items:center;justify-content:center;flex:none}

/* footer */
.site-footer{left:0;top:4204px;width:1200px;height:72px;background:var(--footer)}
.site-footer p{position:absolute;left:100px;top:24px;color:#fff;font-size:13px;font-weight:600}
.socials{position:absolute;right:100px;top:20px;display:flex;gap:12px}
.socials span{width:32px;height:32px;border-radius:50%;background:#fff}
</style>
</head>
<body>

<header class="abs site-header">
  <div class="abs brand">BrightLeap<span class="brand-dot"></span></div>
  <div class="abs contact-bar">
    <span><i class="mini-ico"><svg width="12" height="12" viewBox="0 0 24 24"><path fill="#2e93db" d="M6.6 10.8a15 15 0 006.6 6.6l2.2-2.2a1 1 0 011-.25 11.4 11.4 0 003.6.6 1 1 0 011 1V20a1 1 0 01-1 1A17 17 0 013 4a1 1 0 011-1h3.5a1 1 0 011 1c0 1.25.2 2.45.6 3.6a1 1 0 01-.25 1z"/></svg></i>(+1) 555 010 2040</span>
    <span><i class="mini-ico"><svg width="12" height="12" viewBox="0 0 24 24"><path fill="#2e93db" d="M2 5h20v14H2z"/><path fill="none" stroke="#fff" stroke-width="2" d="M2 5l10 8 10-8"/></svg></i>hello@brightleap.example</span>
  </div>
  <nav class="abs main-nav">
    <span>HOME</span><span>WHO WE ARE</span><span>OUR SERVICES</span><span class="active">BLOG</span><span>NEWS</span><span>CONTACT</span>
  </nav>
</header>

<section class="abs hero" role="img" aria-label="Photo of a team's hands working at a wooden desk with laptop, tablet, phone and charts">
  <div class="abs hero-shade"></div>
</section>
<div class="abs hero-line"></div>
<div class="abs hero-title"><div class="l1">WE HELP PEOPLE</div><div class="l2">HELP THEMSELVES</div></div>
<div class="abs hero-arrow" style="left:22px"><svg width="16" height="16" viewBox="0 0 16 16"><path d="M10 3L5 8l5 5" stroke="#fff" stroke-width="2.4" fill="none"/></svg></div>
<div class="abs hero-arrow" style="left:1140px"><svg width="16" height="16" viewBox="0 0 16 16"><path d="M6 3l5 5-5 5" stroke="#fff" stroke-width="2.4" fill="none"/></svg></div>

<h2 class="abs section-title" style="left:0;top:806px;width:1200px">WHAT IS IT THAT WE DO?</h2>
<p class="abs lead" style="left:250px;top:872px;width:700px">At vero eos et accusamus et iusto odio dignissimos ducimus qui blanditiis praesentium voluptatum deleniti atque corrupti quos dolores et quas molestias excepturi sint occaecati cupiditate non provident.</p>

<div class="abs service" style="left:92px">
  <div class="service-ico"><svg width="40" height="40" viewBox="0 0 40 40" fill="none" stroke="#fff" stroke-width="2.4"><circle cx="20" cy="20" r="6"/><circle cx="9" cy="9" r="4"/><circle cx="31" cy="9" r="4"/><circle cx="9" cy="31" r="4"/><circle cx="31" cy="31" r="4"/><path d="M12 12l4 4M28 12l-4 4M12 28l4-4M28 28l-4-4"/></svg></div>
  <h4>Online Strategy</h4>
  <p>Nam libero tempore, cum soluta nobis est eligendi optio cumque nihildit quo minus quod maxime placeat</p>
</div>
<div class="abs service" style="left:354px">
  <div class="service-ico"><svg width="40" height="40" viewBox="0 0 40 40" fill="none" stroke="#fff" stroke-width="2.4"><rect x="8" y="9" width="24" height="18" rx="2"/><path d="M15 32h10M20 27v5M13 15h14M13 20h9"/></svg></div>
  <h4>Digital Media</h4>
  <p>Nam libero tempore, cum soluta nobis est eligendi optio cumque nihildit quo minus quod maxime placeat</p>
</div>
<div class="abs service" style="left:616px">
  <div class="service-ico"><svg width="40" height="40" viewBox="0 0 40 40" fill="none" stroke="#fff" stroke-width="2.4"><path d="M26 8l6 6-12 12a6 6 0 01-8-8z"/><path d="M23 11l6 6M8 32l4-4"/></svg></div>
  <h4>Inbound Marketing</h4>
  <p>Nam libero tempore, cum soluta nobis est eligendi optio cumque nihildit quo minus quod maxime placeat</p>
</div>
<div class="abs service" style="left:878px">
  <div class="service-ico"><svg width="40" height="40" viewBox="0 0 40 40" fill="none" stroke="#fff" stroke-width="2.4"><path d="M7 31h27M7 31V9"/><path d="M10 26l7-8 6 5 9-11"/></svg></div>
  <h4>Business Analytics</h4>
  <p>Nam libero tempore, cum soluta nobis est eligendi optio cumque nihildit quo minus quod maxime placeat</p>
</div>

<section class="abs who"></section>
<div class="abs who-photo photo" role="img" aria-label="Photo of a business team gathered around a tablet in a meeting"></div>
<div class="abs who-text">
  <h2>WHO WE ARE?</h2>
  <p>We are a direct response company that creates and sells information products and services that millions of people find interesting and important in their lives.</p>
  <p style="margin-top:10px">We are specialized in the self-reliance market and we serve conservative Americans. We are in this business to serve globally and to grow individually. What we serve and inspire are people who need safety, comfort and peace of mind. We deliver empowerment through products that create fertile shortcuts to solutions.</p>
  <div style="margin-top:20px"><span class="btn-pill">READ MORE <svg width="12" height="12" viewBox="0 0 12 12"><circle cx="6" cy="6" r="6" fill="#fff"/><path d="M5 3.5L7.5 6 5 8.5" stroke="#2e93db" stroke-width="1.6" fill="none"/></svg></span></div>
</div>

<section class="abs cta">
  <h2>INTERESTED IN OUR SERVICE NOW?</h2>
  <p>At vero eos et accusamus et iusto odio dignissimos ducimus qui blanditiis praesentium voluptatum deleniti atque.</p>
  <div class="btn-outline">GET A QUOTE</div>
</section>

<h2 class="abs section-title" style="left:0;top:1998px;width:1200px">CASE STUDIES</h2>
<p class="abs lead" style="left:0;top:2060px;width:1200px;font-size:15px;color:#777">We live and breathe direct response marketing.</p>

<article class="abs case" style="left:100px">
  <div class="photo" role="img" aria-label="Photo of a businessman with glowing digital charts" style="background:linear-gradient(135deg,#0d1a2c,#1e3f6b 55%,#4a7fb8)"></div>
  <h3>Great Information Products.</h3>
  <p>At vero eos et accusamus et iusto odio dignissimos ducimus qui blanditiis praesentium voluptatum deleniti atque corrupti quos dolores</p>
  <div class="read-more">READ MORE <i></i></div>
</article>
<article class="abs case" style="left:447px">
  <div class="photo" role="img" aria-label="Photo of colleagues smiling at a tablet in a bright office" style="background:linear-gradient(135deg,#d8d4cf,#9c9087 55%,#5c524b)"></div>
  <h3>Compels People To Act.</h3>
  <p>At vero eos et accusamus et iusto odio dignissimos ducimus qui blanditiis praesentium voluptatum deleniti atque corrupti quos dolores</p>
  <div class="read-more">READ MORE <i></i></div>
</article>
<article class="abs case" style="left:795px">
  <div class="photo" role="img" aria-label="Photo of hands reviewing printed charts on a pink desk" style="background:linear-gradient(135deg,#f4d8dc,#e59aa5 55%,#c9606f)"></div>
  <h3>Deep Research To Offer Simple</h3>
  <p>At vero eos et accusamus et iusto odio dignissimos ducimus qui blanditiis praesentium voluptatum deleniti atque corrupti quos dolores</p>
  <div class="read-more">READ MORE <i></i></div>
</article>

<svg class="abs stats-wave" viewBox="0 0 1200 342" preserveAspectRatio="none">
  <path d="M0 120 C120 80 180 170 330 150 C470 130 560 40 770 45 C900 50 920 120 1000 95 C1070 75 1110 20 1200 -5 V342 H0 Z" fill="#2e93db"/>
  <path d="M0 175 C140 150 200 200 380 185 C520 172 600 110 770 112 C900 114 940 170 1040 150 C1110 136 1160 95 1200 80 V342 H0 Z" fill="#3a9de2" opacity=".6"/>
  <path d="M0 120 C120 80 180 170 330 150 C470 130 560 40 770 45 C900 50 920 120 1000 95 C1070 75 1110 20 1200 -5" fill="none" stroke="#7cc0ef" stroke-width="2"/>
  <g fill="#fff" stroke="#2e93db" stroke-width="2"><circle cx="92" cy="112" r="6"/><circle cx="432" cy="88" r="6"/><circle cx="770" cy="45" r="6"/><circle cx="955" cy="115" r="6"/><circle cx="1130" cy="16" r="6"/></g>
</svg>
<div class="abs stat" style="left:98px"><div class="num">38<small>%</small></div><h4>Impact</h4><p>At vero eos et accusamus et iusto odio dignissimos ducimus qui</p></div>
<div class="abs stat" style="left:364px"><div class="num">65<small>%</small></div><h4>Wisdom</h4><p>At vero eos et accusamus et iusto odio dignissimos ducimus qui</p></div>
<div class="abs stat" style="left:630px"><div class="num">90<small>%</small></div><h4>Team spirit</h4><p>At vero eos et accusamus et iusto odio dignissimos ducimus qui</p></div>
<div class="abs stat" style="left:897px"><div class="num">98<small>%</small></div><h4>Innovation</h4><p>At vero eos et accusamus et iusto odio dignissimos ducimus qui</p></div>

<section class="abs testimonials"></section>
<svg class="abs side-arrow" style="left:30px" width="20" height="30" viewBox="0 0 20 30"><path d="M15 4L5 15l10 11" stroke="#aaa" stroke-width="3" fill="none"/></svg>
<svg class="abs side-arrow" style="left:1150px" width="20" height="30" viewBox="0 0 20 30"><path d="M5 4l10 11-10 11" stroke="#aaa" stroke-width="3" fill="none"/></svg>
<div class="abs client-photo" role="img" aria-label="Portrait photo of a client in a suit"></div>
<div class="abs quote-badge">&rdquo;</div>
<div class="abs testimonial-body">
  <h2>WHAT OUR CLIENTS SAY</h2>
  <blockquote>Nor again is there anyone who loves or pursues or desires to obtain pain of itself, because it is pain but because occasionally circumstances occur in which toil and pain can procure him some great pleasure. To take a trivial example, which of us ever undertakes laborious physical exercise</blockquote>
  <cite><b>PRIYA NANDAN,</b> Creative Manager</cite>
</div>

<svg class="abs team-curve" viewBox="0 0 1200 180" preserveAspectRatio="none"><path d="M0 95 Q600 -20 1200 95 V180 H0 Z" fill="#fff"/></svg>
<h2 class="abs section-title team-title">OUR TEAM &amp; VALUES</h2>
<p class="abs lead team-lead">Nemo enim ipsam voluptatem quia voluptas sit aspernatur aut odit aut fugit, sed quia consequuntur magni dolores eos qui ratione voluptatem sequi nesciunt.</p>

<div class="abs member-frame" style="left:100px"></div>
<div class="abs member-photo a photo" role="img" aria-label="Portrait photo of the company's CEO"></div>
<article class="abs member" style="left:302px">
  <h3>MAREK LIND</h3>
  <div class="role">CEO BrightLeap</div>
  <p>Marek started or was involved in 13 failed businesses before discovering online copywriting. After that, he ended up</p>
  <div class="read-more">READ MORE <i></i></div>
</article>

<div class="abs member-frame" style="left:641px"></div>
<div class="abs member-photo b photo" role="img" aria-label="Portrait photo of the company's cofounder"></div>
<article class="abs member" style="left:834px;width:266px">
  <h3>DANIEL LIND</h3>
  <div class="role">Cofounder &amp; Affiliate Manager BrightLeap</div>
  <p>Since the company's start in late 2012, Daniel grew a network of 5000 affiliates, that dominates affiliate networks survival niche.</p>
  <div class="read-more">READ MORE <i></i></div>
</article>

<section class="abs contact">
  <h2>QUICK CONTACT</h2>
  <p class="sub">At vero eos et accusamus et iusto odio dignissimos ducimus qui blanditiis praesentium.</p>
  <div class="field" style="left:200px;top:183px;width:256px;height:40px">Full Name</div>
  <div class="field" style="left:479px;top:183px;width:248px;height:40px">Email Address</div>
  <div class="field" style="left:741px;top:183px;width:258px;height:40px">Website</div>
  <div class="field" style="left:200px;top:243px;width:799px;height:72px">Message</div>
  <div class="btn-submit">SUBMIT NOW</div>
  <div class="info" style="left:115px">
    <span class="info-ico"><svg width="20" height="22" viewBox="0 0 24 24"><path fill="#2e93db" d="M12 2a7 7 0 00-7 7c0 5 7 13 7 13s7-8 7-13a7 7 0 00-7-7zm0 9.5A2.5 2.5 0 1112 6.5a2.5 2.5 0 010 5z"/></svg></span>
    <span>88 Harbor Lane, Suite 4<br>Westfield, ZX - 40210</span>
  </div>
  <div class="info" style="left:487px">
    <span class="info-ico"><svg width="20" height="20" viewBox="0 0 24 24"><path fill="#2e93db" d="M6.6 10.8a15 15 0 006.6 6.6l2.2-2.2a1 1 0 011-.25 11.4 11.4 0 003.6.6 1 1 0 011 1V20a1 1 0 01-1 1A17 17 0 013 4a1 1 0 011-1h3.5a1 1 0 011 1c0 1.25.2 2.45.6 3.6a1 1 0 01-.25 1z"/></svg></span>
    <span>Phone: (+1) 555 010 2040<br>Fax: (+1) 555 010 2041</span>
  </div>
  <div class="info" style="left:762px">
    <span class="info-ico"><svg width="22" height="22" viewBox="0 0 24 24" fill="none" stroke="#2e93db" stroke-width="2.4"><circle cx="12" cy="12" r="9"/><path d="M12 7v5l3 2"/></svg></span>
    <span>Monday - Saturday &nbsp;:&nbsp; 8:00am - 10:00pm<br>Sunday &nbsp;:&nbsp; 10am - 3pm</span>
  </div>
</section>

<footer class="abs site-footer">
  <p>&copy; Copyright 2018 BrightLeap. All Rights Reserved.</p>
  <div class="socials"><span></span><span></span><span></span><span></span></div>
</footer>

</body>
</html>
```